Wine Label for a White and a Red Wine from Italy

We have a very good idea of what we want with artwork. We need you to please design a 'template' with the text so we can change out the artwork from year to year. Samples are shown of what we are looking for. We are looking for options with the two basic designs. Brand name of wine is: Valora di Castegno. Both wines are in a light green Bordeaux-style bottle (note: we don't show a light green bottle in the mockup but please remember the bottle is light green). Artwork is provided. We'd like to see either the green or blue butterfly on the white wine, the red butterfly is for the red wine. Please base the design on the attached label from Brailey and/or the attached label from Chateau Mervanges.

Target Market(s)

Millennials, women

Requirements
Must have
• The artwork (butterflies) attached.
Nice to have
• Elegant, readable fonts. Please make the text so it can be changed by the printer. Please make it so the artwork can be changed too.

```html
<!DOCTYPE html>
<html lang="en">
<head>
<meta charset="utf-8">
<title>Valora di Castegno – Barrel Select Labels</title>
<link rel="stylesheet" href="https://fonts.googleapis.com/css2?family=Old+Standard+TT:wght@400&display=swap">
<style>
  :root {
    --page-bg: #f5f5f5;
    --label-bg: #ffffff;
    --label-edge: #e1e1e1;
    --ink: #1c1c1c;
    --art-light: #f6cf6a;
    --art-deep: #eaa631;
  }
  * { margin: 0; padding: 0; box-sizing: border-box; }
  html, body {
    width: 1200px;
    height: 1083px;
    overflow: hidden;
    background: var(--page-bg);
  }
  body {
    position: relative;
    font-family: "Old Standard TT", "Times New Roman", serif;
    font-weight: 400;
    color: var(--ink);
  }
  .label {
    position: absolute;
    top: 226px;
    width: 440px;
    height: 631px;
    background: var(--label-bg);
    border: 1px solid var(--label-edge);
    text-align: center;
  }
  .label--bianco { left: 130px; }
  .label--rosso { left: 630px; }

  .label > * {
    position: absolute;
    left: 0;
    right: 0;
    font-weight: 400;
    line-height: 1;
  }

  .brand-name {
    top: 34px;
    font-size: 58px;
    letter-spacing: 0.2em;
    padding-left: 0.2em;
  }
  .brand-sub {
    top: 96px;
    font-size: 22px;
  }
  .artwork {
    top: 130px;
    left: 80px;
    right: auto;
    width: 280px;
    height: 240px;
    background: linear-gradient(160deg, var(--art-light), var(--art-deep));
  }
  .cuvee {
    top: 394px;
    font-size: 27px;
    letter-spacing: 0.01em;
  }
  .vintage {
    top: 436px;
    font-size: 22px;
  }
  .varietal {
    top: 470px;
    font-size: 27px;
  }
  .origin {
    top: 502px;
    font-size: 21px;
  }
  .producer {
    top: 544px;
    font-size: 19px;
    line-height: 27px;
  }
</style>
</head>
<body>

  <section class="label label--bianco">
    <h1 class="brand-name">VALORA</h1>
    <p class="brand-sub">di Castegno</p>
    <div class="artwork" role="img" aria-label="Replaceable artwork: teal-blue butterfly on a golden painted brushstroke"></div>
    <h2 class="cuvee">BARREL SELECT</h2>
    <p class="vintage">2018</p>
    <p class="varietal">Bianco</p>
    <p class="origin">Piemonte, Itely</p>
    <p class="producer">Artisanlly Crafted by Cantina Quattro Colli<br>sustainably farmed</p>
  </section>

  <section class="label label--rosso">
    <h1 class="brand-name">VALORA</h1>
    <p class="brand-sub">di Castegno</p>
    <div class="artwork" role="img" aria-label="Replaceable artwork: red butterfly on a golden painted brushstroke"></div>
    <h2 class="cuvee">BARREL SELECT</h2>
    <p class="vintage">2018</p>
    <p class="varietal">Rosso</p>
    <p class="origin">Piemonte, Itely</p>
    <p class="producer">Artisanlly Crafted by Cantina Quattro Colli<br>sustainably farmed</p>
  </section>

</body>
</html>
```